Valmora Holdings - Tidal Crest Car Wash automatic car wash signage

We are wanting to have a new automatic car wash sign designed. Our current one is dated and there are numerous options that are no longer available. We like the look of a clean sharp design in keeping with the Tidal Crest colours; orange and blues. The sign should have the Ultimate and Premium options, the "Tidal Crest" and Tidal Crest Car Wash designed in a clean, concise and cool manner.

Font styles to use
Sans Serif

Colors
f37122
3276b5
0255a3
34a7d8

Requirements
Must have
• This project must have the Ultimate and Premium options, the "bucket" and the Tidal Crest Car Wash title. The orange is a key colour with blues for water.

```html
<!DOCTYPE html>
<html lang="en">
<head>
<meta charset="UTF-8">
<title>Tidal Crest Car Wash – Wash Menu Sign</title>
<link rel="stylesheet" href="https://fonts.googleapis.com/css2?family=Orbitron:wght@900&family=Saira+Condensed:wght@700&display=swap">
<style>
  :root {
    --orange: #f37122;
    --orange-deep: #d9540e;
    --blue-mid: #3276b5;
    --blue-deep: #0255a3;
    --blue-sky: #34a7d8;
    --navy: #0b1a4a;
    --row-blue: #2a35a0;
    --gold: #e6d21a;
    --ink: #000000;
    --white: #ffffff;
    --page: #e9ecf0;
  }
  * { margin: 0; padding: 0; box-sizing: border-box; }
  html, body { width: 1200px; height: 801px; overflow: hidden; background: var(--page); }

  .sign {
    position: absolute; left: 0; top: 117px;
    width: 1200px; height: 566px;
    background: var(--navy);
    overflow: hidden;
  }
  .water-photo {
    position: absolute; inset: 0;
    background:
      radial-gradient(ellipse 60% 50% at 50% 75%, rgba(220,238,252,0.85), transparent 70%),
      radial-gradient(ellipse 30% 40% at 92% 60%, rgba(2,85,163,0.8), transparent 70%),
      linear-gradient(180deg, #0a1540 0%, #14306e 22%, var(--blue-mid) 48%, #8fc0e8 72%, var(--blue-sky) 100%);
  }

  .brand-mark {
    position: absolute; left: 32px; top: 28px; width: 96px;
    font-family: "Saira Condensed", sans-serif; font-weight: 700;
    font-size: 25px; line-height: 24px; color: var(--orange);
    text-align: center;
  }

  .title {
    position: absolute; left: 130px; width: 940px;
    font-family: "Orbitron", sans-serif; font-weight: 900;
    color: var(--orange); text-align: center; line-height: 1;
    -webkit-text-stroke: 1.5px var(--white);
    text-shadow: 4px 4px 0 var(--ink);
  }
  .title--top { top: 28px; font-size: 60px; letter-spacing: 2px; }
  .title--bottom { top: 94px; font-size: 66px; letter-spacing: 3px; }

  .tier {
    position: absolute; top: 108px; width: 161px; height: 56px;
    border: 2px solid var(--gold); border-radius: 28px;
    background: var(--ink); color: var(--white);
    font-family: "Orbitron", sans-serif; font-weight: 900;
    text-align: center; padding-top: 6px;
  }
  .tier__name { font-size: 15px; letter-spacing: 1px; line-height: 16px; }
  .tier__price { font-size: 24px; line-height: 26px; }
  .tier--ultimate { left: 198px; }
  .tier--premium { left: 837px; }

  .features { position: absolute; top: 174px; left: 0; width: 1200px; list-style: none; }
  .feature { position: absolute; left: 0; width: 1200px; height: 30px; }
  .feature__name {
    position: absolute; left: 400px; width: 404px; height: 30px;
    background: var(--row-blue); border: 2px solid var(--gold); border-radius: 15px;
    color: var(--white); font-family: "Saira Condensed", sans-serif; font-weight: 700;
    font-size: 16px; line-height: 26px; text-align: center; letter-spacing: 0.3px;
  }
  .pill {
    position: absolute; width: 160px; height: 30px;
    border: 2px solid var(--ink); border-radius: 15px;
    background: linear-gradient(180deg, var(--orange-deep) 0%, var(--orange) 30%, #ffe6d6 50%, var(--orange) 72%, var(--orange-deep) 100%);
    box-shadow: 2px 3px 0 rgba(0,0,0,0.6);
    display: flex; align-items: center; justify-content: center;
  }
  .pill--ultimate { left: 196px; }
  .pill--premium { left: 842px; }
  .tick { width: 26px; height: 22px; }
</style>
</head>
<body>
<main class="sign">
  <div class="water-photo" role="img" aria-label="Splashing blue water photograph behind the menu"></div>

  <div class="brand-mark">Tidal<br>Crest</div>

  <h1 class="title title--top">TIDAL CREST CAR</h1>
  <div class="title title--bottom">WASH</div>

  <div class="tier tier--ultimate"><div class="tier__name">ULTIMATE</div><div class="tier__price">$1400</div></div>
  <div class="tier tier--premium"><div class="tier__name">PREMIUM</div><div class="tier__price">$1200</div></div>

  <svg width="0" height="0" style="position:absolute">
    <defs><symbol id="tick" viewBox="0 0 26 22"><path d="M2 11 L9 19 L24 2" fill="none" stroke="#000" stroke-width="3.2" stroke-linecap="round" stroke-linejoin="round"/></symbol></defs>
  </svg>

  <ul class="features">
    <li class="feature" style="top:0"><span class="pill pill--ultimate"><svg class="tick"><use href="#tick"/></svg></span><span class="feature__name">WINDSHIELD &amp; FRONT BUG WASH</span><span class="pill pill--premium"></span></li>
    <li class="feature" style="top:38px"><span class="pill pill--ultimate"><svg class="tick"><use href="#tick"/></svg></span><span class="feature__name">UNDER CARRIAGE &amp; WHEEL BLASTER</span><span class="pill pill--premium"><svg class="tick"><use href="#tick"/></svg></span></li>
    <li class="feature" style="top:76px"><span class="pill pill--ultimate"><svg class="tick"><use href="#tick"/></svg></span><span class="feature__name">EXTRA PASS OF HIGH PRESSURE WASH</span><span class="pill pill--premium"></span></li>
    <li class="feature" style="top:114px"><span class="pill pill--ultimate"><svg class="tick"><use href="#tick"/></svg></span><span class="feature__name">TRY FORM CONDITIONER / CLEANER</span><span class="pill pill--premium"></span></li>
    <li class="feature" style="top:152px"><span class="pill pill--ultimate"><svg class="tick"><use href="#tick"/></svg></span><span class="feature__name">SIDE KICK DRYERS</span><span class="pill pill--premium"><svg class="tick"><use href="#tick"/></svg></span></li>
    <li class="feature" style="top:190px"><span class="pill pill--ultimate"><svg class="tick"><use href="#tick"/></svg></span><span class="feature__name">WAX / SURFACE PROTECTANT</span><span class="pill pill--premium"></span></li>
    <li class="feature" style="top:228px"><span class="pill pill--ultimate"><svg class="tick"><use href="#tick"/></svg></span><span class="feature__name">ON BOARD OVERHEAD DRYER</span><span class="pill pill--premium"><svg class="tick"><use href="#tick"/></svg></span></li>
    <li class="feature" style="top:266px"><span class="pill pill--ultimate"><svg class="tick"><use href="#tick"/></svg></span><span class="feature__name">TWO PASSES OF PRE-SOAK</span><span class="pill pill--premium"><svg class="tick"><use href="#tick"/></svg></span></li>
    <li class="feature" style="top:304px"><span class="pill pill--ultimate"><svg class="tick"><use href="#tick"/></svg></span><span class="feature__name">HIGH PRESSURE WASH PASS</span><span class="pill pill--premium"><svg class="tick"><use href="#tick"/></svg></span></li>
    <li class="feature" style="top:342px"><span class="pill pill--ultimate"><svg class="tick"><use href="#tick"/></svg></span><span class="feature__name">SPOT FREE RIMSE</span><span class="pill pill--premium"><svg class="tick"><use href="#tick"/></svg></span></li>
  </ul>
</main>
</body>
</html>
```